Business Cards for company that supports physicians that do medical research

Need to create a business card for Halvern Studies (www.valtrexstudies.example), a company devoted to supporting physicians who conduct medical research. The form of the card should match the message of research and information quest. I have provided the logo of the company as an uploaded file. Designs should be simple and slick aimed at very high end clients.

Target Market(s)

Medical doctors that are also researchers

Industry/Entity Type

Medical

Contact Information for Business Card

Should feature logo and fields for personal info:
Name/title
Phone /email

Font styles to use
Serif
Sans Serif

Requirements
Must have
• Halvern logo and fields for personal info:
• Name: Corwin Abbatelli
• Title: VP Research and Senior Analyst
• Phone: 555-203-7416
• email: info@halvernstudies.example
Nice to have
• Interesting cards that I've seen:
• 1- all black/charcoal or very dark background
• 2- Plastic - semi-transparent
• 3- non-standard height-width ratios
• 4- Functional cards -- USB drive incorporated
Should not have
• Too busy; needs to stay very simple

```html
<!DOCTYPE html>
<html lang="en">
<head>
<meta charset="utf-8">
<title>Halvern Studies — Business Card</title>
<link rel="stylesheet" href="https://fonts.googleapis.com/css2?family=Cinzel:wght@400;600&display=swap">
<style>
  :root {
    --stage-bg: #3b3b3d;
    --card-top: #1c1c1d;
    --card-bottom: #0b0b0c;
    --frame-line: #d9d9d9;
    --ink: #f1f1f1;
    --ink-soft: #cfcfcf;
    --brand-green: #5cc04a;
    --brand-blue: #1f8ad6;
  }
  * { margin: 0; padding: 0; box-sizing: border-box; }
  html, body {
    width: 1200px;
    height: 900px;
    overflow: hidden;
    background: var(--stage-bg);
  }
  body {
    display: flex;
    align-items: center;
    justify-content: center;
    font-family: "Cinzel", serif;
    color: var(--ink);
  }
  .business-card {
    position: relative;
    width: 900px;
    height: 514px;
    background: linear-gradient(160deg, var(--card-top), var(--card-bottom));
    box-shadow: 0 18px 40px rgba(0,0,0,0.45);
  }
  .card-frame {
    position: absolute;
    inset: 24px;
    border: 2px solid var(--frame-line);
    display: flex;
    flex-direction: column;
    align-items: center;
    text-align: center;
  }
  .brand {
    margin-top: 64px;
    display: flex;
    align-items: center;
    gap: 16px;
  }
  .brand-dot {
    width: 20px;
    height: 20px;
    border-radius: 50%;
    background: var(--brand-blue);
  }
  .brand-name {
    font-weight: 600;
    font-size: 44px;
    line-height: 1.1;
    letter-spacing: 2px;
    color: var(--brand-green);
  }
  .person-name {
    margin-top: 62px;
    font-weight: 600;
    font-size: 32px;
    line-height: 1.2;
    letter-spacing: 1.5px;
  }
  .person-title {
    margin-top: 6px;
    font-size: 16px;
    letter-spacing: 1.5px;
    color: var(--ink-soft);
  }
  .divider {
    margin-top: 20px;
    width: 260px;
    height: 8px;
  }
  .contact {
    margin-top: 20px;
    font-size: 15px;
    letter-spacing: 1.5px;
    line-height: 1.9;
    color: var(--ink-soft);
  }
</style>
</head>
<body>
  <article class="business-card">
    <div class="card-frame">
      <div class="brand">
        <span class="brand-dot" aria-hidden="true"></span>
        <span class="brand-name">Halvern Studies</span>
      </div>
      <h1 class="person-name">Corwin Abbatelli</h1>
      <p class="person-title">VP Research and Senior Analyst</p>
      <svg class="divider" viewBox="0 0 260 8" aria-hidden="true">
        <defs>
          <linearGradient id="rule-fade" x1="0" x2="1">
            <stop offset="0" stop-color="#cfcfcf" stop-opacity="0"/>
            <stop offset="0.5" stop-color="#cfcfcf" stop-opacity="1"/>
            <stop offset="1" stop-color="#cfcfcf" stop-opacity="0"/>
          </linearGradient>
        </defs>
        <rect x="0" y="3.5" width="260" height="1" fill="url(#rule-fade)"/>
        <circle cx="130" cy="4" r="2.6" fill="#e6e6e6"/>
      </svg>
      <div class="contact">
        <p class="contact-email">info@halvernstudies.example</p>
        <p class="contact-phone">555-203-7416</p>
      </div>
    </div>
  </article>
</body>
</html>
```